Business Card / Email signature with new logo
New logo for Real estate Agent
Business Card / Email signature with new logo - Real Estate
Creative Brief
Professional
Lena Vortham
Realtor
4817 Bellgrove Lane, Ste. 300 Allen, TX 75098
Lena@LenaVorthamRealty.example
www.LenaVorthamRealty.example
License #0382741
I am looking for something that compliments my new logo.. I like the logo in the black background but have sent both for utilization. Ijust want a nice appealing card.
I would like to see the logo as one side of the card and the information on the back. I need to have the Dunmore Pike logo on the card as well on the back and it needs to be noted that : Each Dunmore Pike Office is Independently owned & Operated. I would also like to have the Realtor and HPX symbol included on the the card.

```html
<!DOCTYPE html>
<html lang="en">
<head>
<meta charset="utf-8">
<title>Lena Vortham Realty – Business Cards</title>
<link rel="stylesheet" href="https://fonts.googleapis.com/css2?family=Open+Sans:ital,wght@0,400;0,600;0,700;1,700&family=Playfair+Display:ital,wght@0,700;1,700&display=swap">
<style>
  :root{
    --stage:#3a3a3a;
    --white:#ffffff;
    --black:#0b0b0b;
    --ink:#1d1d1d;
    --red:#c8202a;
    --gold:#c99a4e;
    --gold-light:#f0d49a;
    --photo-a:#c9c2bb;
    --photo-b:#6d6a70;
  }
  *{margin:0;padding:0;box-sizing:border-box}
  html,body{width:1200px;height:811px;overflow:hidden}
  body{background:var(--stage);position:relative;font-family:"Open Sans",Arial,sans-serif}

  .card{position:absolute;border-radius:14px;overflow:hidden}
  .card--light{background:var(--white);color:var(--ink)}
  .card--dark{background:var(--black);color:var(--white)}
  .card--info{left:52px;width:558px;height:292px}
  .card--logo{left:640px;width:516px;height:292px}
  .row-top{top:54px}
  .row-bottom{top:402px}

  .wordmark{position:absolute;font-family:"Playfair Display",Georgia,serif;font-weight:700;white-space:nowrap;display:flex;align-items:center;gap:10px}
  .wordmark__dot{display:inline-block;border-radius:50%;background:currentColor}
  .card--light .wordmark{color:var(--ink)}
  .card--dark .wordmark{color:var(--gold)}
  .tagline{position:absolute;font-family:"Playfair Display",Georgia,serif;font-style:italic;font-weight:700;color:var(--red);white-space:nowrap}
  .card--dark .tagline{color:var(--gold-light)}

  .card--info .wordmark{left:26px;top:26px;font-size:24px}
  .card--info .wordmark__dot{width:12px;height:12px}
  .card--info .tagline{left:28px;top:64px;font-size:11px}

  .card--logo .wordmark{left:0;right:0;justify-content:center;top:92px;font-size:44px}
  .card--logo .wordmark__dot{width:20px;height:20px}
  .card--logo .tagline{left:0;right:0;text-align:center;top:162px;font-size:19px}
  .address{position:absolute;left:0;right:0;top:240px;text-align:center;font-size:11.5px}

  .contact{position:absolute;left:30px;top:96px;list-style:none;font-size:11px;line-height:19px}
  .contact li{display:flex;align-items:center;gap:7px}
  .contact svg{width:11px;height:11px;flex:none;fill:currentColor}
  .disclaimer{position:absolute;left:30px;top:156px;font-size:11px;line-height:14px;width:220px}

  .affiliations{position:absolute;left:28px;top:196px;display:flex;align-items:center;gap:8px;color:var(--ink)}
  .card--dark .affiliations{top:206px}
  .badge-square{width:22px;height:22px;background:var(--ink);border-radius:2px}
  .badge-pill{width:38px;height:22px;border-radius:4px;background:var(--ink)}
  .affil-name{font-size:14px;font-weight:700}
  .brokerage{font-size:11px;font-weight:700;letter-spacing:.5px;margin-left:26px;text-transform:uppercase}

  .portrait{position:absolute;left:300px;top:18px;width:212px;height:210px;background:radial-gradient(circle at 50% 35%,var(--photo-a) 0,var(--photo-a) 28%,var(--photo-b) 70%);border-radius:4px}

  .swoosh{position:absolute;left:0;top:0;width:558px;height:292px}
  .signature{position:absolute;right:30px;top:256px;font-size:13px;font-weight:700;color:var(--black)}
  .signature em{font-style:italic}
</style>
</head>
<body>

<svg width="0" height="0" style="position:absolute">
  <defs>
    <linearGradient id="goldBand" x1="0" y1="0" x2="1" y2="0">
      <stop offset="0" stop-color="#8a6326"/>
      <stop offset=".35" stop-color="#f0d49a"/>
      <stop offset=".7" stop-color="#c99a4e"/>
      <stop offset="1" stop-color="#f3dcaa"/>
    </linearGradient>
  </defs>
</svg>

<section class="card card--light card--info row-top">
  <div class="wordmark">Lena Vortham Realty<span class="wordmark__dot"></span></div>
  <div class="tagline">Your Trusted Guide to Texas Homes</div>
  <div class="portrait" role="img" aria-label="Portrait photo of Lena Vortham"></div>
  <svg class="swoosh" viewBox="0 0 558 292" aria-hidden="true">
    <path d="M0 228 Q240 196 558 214 L558 292 L0 292 Z" fill="#ffffff"/>
    <path d="M0 252 Q250 218 558 232 L558 292 L0 292 Z" fill="url(#goldBand)"/>
    <path d="M0 252 Q250 218 558 232" fill="none" stroke="#2a2a2a" stroke-width="2"/>
  </svg>
  <ul class="contact">
    <li><svg viewBox="0 0 24 24"><path d="M6.6 10.8a15 15 0 0 0 6.6 6.6l2.2-2.2a1 1 0 0 1 1-.25 11.4 11.4 0 0 0 3.6.57 1 1 0 0 1 1 1V20a1 1 0 0 1-1 1A17 17 0 0 1 3 4a1 1 0 0 1 1-1h3.5a1 1 0 0 1 1 1c0 1.25.2 2.45.57 3.57a1 1 0 0 1-.25 1z"/></svg>972-555-0148</li>
    <li><svg viewBox="0 0 24 24"><path d="M2 5h20v14H2z M4 7v.5l8 5 8-5V7l-8 5z"/></svg>Lena@LenaVorthamRealty.example</li>
    <li><svg viewBox="0 0 24 24"><circle cx="12" cy="12" r="10"/></svg>www.LenaVorthamRealty.example</li>
  </ul>
  <p class="disclaimer">Each Dunmore Pike Office<br>is Independently owned &amp; Operated</p>
  <div class="affiliations">
    <span class="badge-square"></span>
    <span class="badge-pill"></span>
    <span class="affil-name">HPX</span>
    <span class="brokerage">Dunmore Pike</span>
  </div>
  <div class="signature"><em>Lena Vortham</em>, Realtor</div>
</section>

<section class="card card--light card--logo row-top">
  <div class="wordmark">Lena Vortham Realty<span class="wordmark__dot"></span></div>
  <div class="tagline">Your Trusted Guide to Texas Homes</div>
  <p class="address">4817 Bellgrove Lane, Ste. 300 Allen, TX 75098</p>
</section>

<section class="card card--dark card--info row-bottom">
  <div class="wordmark">Lena Vortham Realty<span class="wordmark__dot"></span></div>
  <div class="tagline">Your Trusted Guide to Texas Homes</div>
  <div class="portrait" role="img" aria-label="Portrait photo of Lena Vortham"></div>
  <svg class="swoosh" viewBox="0 0 558 292" aria-hidden="true">
    <path d="M0 198 Q240 176 558 210 L558 292 L0 292 Z" fill="#ffffff"/>
    <path d="M0 252 Q250 218 558 232 L558 292 L0 292 Z" fill="url(#goldBand)"/>
    <path d="M0 252 Q250 218 558 232" fill="none" stroke="#2a2a2a" stroke-width="2"/>
  </svg>
  <ul class="contact">
    <li><svg viewBox="0 0 24 24"><path d="M6.6 10.8a15 15 0 0 0 6.6 6.6l2.2-2.2a1 1 0 0 1 1-.25 11.4 11.4 0 0 0 3.6.57 1 1 0 0 1 1 1V20a1 1 0 0 1-1 1A17 17 0 0 1 3 4a1 1 0 0 1 1-1h3.5a1 1 0 0 1 1 1c0 1.25.2 2.45.57 3.57a1 1 0 0 1-.25 1z"/></svg>972-555-0148</li>
    <li><svg viewBox="0 0 24 24"><path d="M2 5h20v14H2z M4 7v.5l8 5 8-5V7l-8 5z"/></svg>Lena@LenaVorthamRealty.example</li>
    <li><svg viewBox="0 0 24 24"><circle cx="12" cy="12" r="10"/></svg>www.LenaVorthamRealty.example</li>
  </ul>
  <p class="disclaimer">Each Dunmore Pike Office<br>is Independently owned &amp; Operated</p>
  <div class="affiliations">
    <span class="badge-square"></span>
    <span class="badge-pill"></span>
    <span class="affil-name">HPX</span>
    <span class="brokerage">Dunmore Pike</span>
  </div>
  <div class="signature"><em>Lena Vortham</em>, Realtor</div>
</section>

<section class="card card--dark card--logo row-bottom">
  <div class="wordmark">Lena Vortham Realty<span class="wordmark__dot"></span></div>
  <div class="tagline">Your Trusted Guide to Texas Homes</div>
  <p class="address">4817 Bellgrove Lane, Ste. 300 Allen, TX 75098</p>
</section>

</body>
</html>
```